New website: Brixelvane.com

We need to build a website for our small travel agency.
We want to be able to upload our brochures and offer our tours on site. No online payments involved yet.

We want to create an exact copy of another website: www.tolmerhaven.is, but with our own information and products. We like that design very much.

We are not going to do any sales via the website as the website above, but instead we want to show in the same style and everything the different tours that we offer.

We need to be able to modify tours: tour pictures, info, add videos, text, etc.

We need the website in English and Spanish. We can provide the Spanish translation.

We would advice you to create a copy of that website, with the text to be editable by us.
We own the website www.brixelvane.com and need that the designer uploads it and makes it work as well.

We have uploaded some pictures that can be used as place markers.

I HAVE UPLOADED OUR BROCHURE DEMO SO YOU CAN GET MORE INFO IN ENGLISH ABOUT US AND MORE PICTURES.

PLEASE REMEMBER THAT THE WEBSITE ¨MOVES¨ when you resize it! Specially the pictures get ¨bigger¨ or smaller¨ when you resize. The same applies to the logos :-)

Once you have created the front page just as the original website I will select it and then we can put the real info and extra pages :-)

Target Market(s)

Tourists, international people traveling.

Industry/Entity Type

Tourism

Coding

Coded - Design and coding required

Number of Pages Required

5+ page

Font styles to use
Sans Serif

Colors
ffffff

Requirements
Must have
• Exactly the same layout of the website mentioned (www.tolmerhaven.is)
• Everything the same, but with our own logo, texts and photos.
• HOME
• TOURS
• GROUPS
• OUR MOST POPULAR TOURS

```html
<!DOCTYPE html>
<html lang="es">
<head>
<meta charset="utf-8">
<title>Brixelvane — Tours</title>
<link rel="stylesheet" href="https://fonts.googleapis.com/css2?family=Arimo:ital,wght@0,400;0,700;1,400&family=PT+Serif:ital@1&display=swap">
<style>
:root{
  --ink:#1a1a1a;
  --text:#555555;
  --red:#c8192b;
  --white:#ffffff;
  --band-a:#f4f4f4;
  --band-b:#e9e9e9;
  --band-c:#f6f6f6;
  --footer:#0b0b0b;
  --line:#d9d9d9;
  --sky:#4f88c6;
  --sky-light:#b8d2ea;
  --snow:#e6ecf1;
  --rock:#5d6a70;
  --lake:#2f7487;
  --ground:#3a3f38;
}
*{margin:0;padding:0;box-sizing:border-box}
html,body{width:1200px;height:3557px;overflow:hidden;background:var(--white)}
body{position:relative;font-family:"Arimo",Arial,sans-serif;color:var(--ink)}

/* header */
.site-header{position:absolute;left:0;top:0;width:1200px;height:85px;background:var(--white)}
.brand{position:absolute;left:157px;top:22px;display:flex;align-items:center;gap:9px}
.brand-name{font-weight:700;font-size:30px;letter-spacing:1px;color:var(--ink)}
.brand-dot{width:16px;height:16px;border-radius:50%;background:var(--red)}
.main-nav a{position:absolute;top:33px;font-size:15px;color:var(--ink);text-decoration:none}
.search-icon{position:absolute;left:1024px;top:32px}

/* photo placeholders */
.photo{position:absolute;overflow:hidden}
.photo-landscape{background:linear-gradient(180deg,var(--sky) 0%,var(--sky-light) 34%,var(--snow) 46%,var(--rock) 58%,var(--lake) 72%,#1f5566 100%)}
.photo-trail{background:linear-gradient(180deg,#5b8fc4 0%,#c2d5e6 38%,var(--rock) 58%,#6a6a5c 78%,#4a4a42 100%)}
.photo-snow{background:linear-gradient(180deg,#3e78b8 0%,#a9c6e2 36%,var(--snow) 54%,#6f7c80 74%,#3a4246 100%)}
.photo-towers{background:linear-gradient(180deg,#3f7fc4 0%,#8fb8e2 30%,var(--snow) 46%,#6c7980 60%,#7e8b8a 76%,#3b3a35 100%)}

/* hero */
.hero-caption{position:absolute;color:var(--white)}
.hero-caption .word{font-family:"PT Serif",Georgia,serif;font-style:italic;font-size:38px;line-height:1}
.hero-caption .sub{font-size:17px;letter-spacing:.5px;margin-top:6px}

/* popular tours */
.section-title{position:absolute;left:0;width:1200px;top:604px;text-align:center;font-size:33px;font-weight:400;color:var(--ink)}
.tab{position:absolute;top:676px;font-size:12.5px;font-style:italic;color:var(--ink);white-space:nowrap}
.tab.is-active{color:var(--red)}
.tab-rule{position:absolute;left:157px;top:700px;width:886px;height:1px;background:var(--line)}
.tab-mark{position:absolute;left:160px;top:699px;width:128px;height:2px;background:var(--red)}
.tour-card{position:absolute;width:280px}
.tour-photo{position:relative;width:280px;height:227px}
.tour-title{margin-top:17px;font-size:19px;font-weight:700;color:var(--ink)}
.tour-length{margin-top:5px;font-size:13px;color:var(--text)}
.tour-price{margin-top:6px;font-size:14px;color:var(--red)}

.btn{position:absolute;display:flex;align-items:center;justify-content:center;border:1.5px solid var(--red);color:var(--red);font-size:12.5px;background:transparent;white-space:nowrap}

/* info bands */
.band{position:absolute;left:0;width:1200px;overflow:hidden}
.band-heading{position:absolute;font-size:23px;font-weight:700;letter-spacing:.5px;color:var(--ink)}
.band-copy{position:absolute;width:360px;font-size:11.5px;line-height:19px;color:var(--text)}
.cutout{position:absolute}

/* partners */
.partner{position:absolute}

/* footer */
.site-footer{position:absolute;left:0;top:3250px;width:1200px;height:307px;background:var(--footer);color:#bdbdbd}
.footer-brand{position:absolute;left:157px;top:50px;width:112px;height:112px;border:2px solid var(--white);border-radius:50%;display:flex;align-items:center;justify-content:center}
.footer-brand span{font-weight:700;font-size:13px;color:var(--white);letter-spacing:.5px}
.footer-col{position:absolute;top:40px;font-size:12px;line-height:29px;text-transform:uppercase}
.footer-contact{position:absolute;left:854px;top:42px;font-size:12px;line-height:15px}
.footer-contact .name{color:var(--white);margin-bottom:6px}
.footer-contact .gap{height:12px}
.footer-rule{position:absolute;left:157px;top:253px;width:886px;height:1px;background:#2e2e2e}
.copyright{position:absolute;left:157px;top:275px;font-size:10.5px;color:#8a8a8a}
.social{position:absolute;top:273px;width:14px;height:14px;border-radius:50%;background:#6f6f6f}
</style>
</head>
<body>

<header class="site-header">
  <div class="brand"><span class="brand-dot"></span><span class="brand-name">BRIXELVANE</span></div>
  <nav class="main-nav">
    <a style="left:502px">Home</a>
    <a style="left:574px">Tours</a>
    <a style="left:643px">Groups</a>
    <a style="left:726px">Rent a Car</a>
    <a style="left:828px">Flight</a>
    <a style="left:897px">Contact</a>
  </nav>
  <svg class="search-icon" width="18" height="18" viewBox="0 0 18 18"><circle cx="7" cy="7" r="5.5" fill="none" stroke="#666" stroke-width="1.8"/><line x1="11" y1="11" x2="16.5" y2="16.5" stroke="#666" stroke-width="2"/></svg>
</header>

<section class="hero">
  <div class="photo photo-landscape" style="left:0;top:85px;width:572px;height:434px" role="img" aria-label="Turquoise lake with snowy mountain peaks and white clouds"></div>
  <div class="hero-caption" style="left:153px;top:405px"><div class="word">Water</div><div class="sub">BRIXELVANE</div></div>

  <div class="photo photo-trail" style="left:577px;top:85px;width:623px;height:213px" role="img" aria-label="Travellers walking on a trail near a mountain lake"></div>
  <div class="hero-caption" style="left:597px;top:212px"><div class="word">FUN</div><div class="sub">BRIXELVANE</div></div>

  <div class="photo photo-snow" style="left:577px;top:303px;width:623px;height:216px" role="img" aria-label="Snow capped mountains seen from a car window"></div>
  <div class="hero-caption" style="left:597px;top:438px"><div class="word">Snow</div><div class="sub">BRIXELVANE</div></div>
</section>

<section class="popular">
  <h2 class="section-title">Our most popular tours</h2>
  <span class="tab is-active" style="left:170px">Popular Tours</span>
  <span class="tab" style="left:284px">Day Tours</span>
  <span class="tab" style="left:378px">Travel by Air Tours</span>
  <span class="tab" style="left:518px">Self Drive Tours</span>
  <span class="tab" style="left:648px">Adventures Tours</span>
  <span class="tab" style="left:792px">Customize Tours</span>
  <span class="tab" style="left:975px">Transfer</span>
  <div class="tab-rule"></div>
  <div class="tab-mark"></div>

  <article class="tour-card" style="left:157px;top:731px"><div class="tour-photo photo-towers" role="img" aria-label="Hikers before granite mountain towers"></div><div class="tour-title">Northern Lights</div><div class="tour-length">length: 3 - 5 hours</div><div class="tour-price">6.400 ISK</div></article>
  <article class="tour-card" style="left:460px;top:731px"><div class="tour-photo photo-towers" role="img" aria-label="Hikers before granite mountain towers"></div><div class="tour-title">Northern Lights</div><div class="tour-length">length: 3 - 5 hours</div><div class="tour-price">6.400 ISK</div></article>
  <article class="tour-card" style="left:763px;top:731px"><div class="tour-photo photo-towers" role="img" aria-label="Hikers before granite mountain towers"></div><div class="tour-title">Northern Lights</div><div class="tour-length">length: 3 - 5 hours</div><div class="tour-price">6.400 ISK</div></article>
  <article class="tour-card" style="left:157px;top:1079px"><div class="tour-photo photo-towers" role="img" aria-label="Hikers before granite mountain towers"></div><div class="tour-title">Northern Lights</div><div class="tour-length">length: 3 - 5 hours</div><div class="tour-price">6.400 ISK</div></article>
  <article class="tour-card" style="left:460px;top:1079px"><div class="tour-photo photo-towers" role="img" aria-label="Hikers before granite mountain towers"></div><div class="tour-title">Northern Lights</div><div class="tour-length">length: 3 - 5 hours</div><div class="tour-price">6.400 ISK</div></article>
  <article class="tour-card" style="left:763px;top:1079px"><div class="tour-photo photo-towers" role="img" aria-label="Hikers before granite mountain towers"></div><div class="tour-title">Northern Lights</div><div class="tour-length">length: 3 - 5 hours</div><div class="tour-price">6.400 ISK</div></article>

  <div class="btn" style="left:488px;top:1438px;width:226px;height:43px">View all our Popular Tours</div>
</section>

<section class="band" style="top:1547px;height:391px;background:var(--band-a)">
  <div class="cutout" style="left:160px;top:30px;width:300px;height:320px;border-radius:16px;background:linear-gradient(160deg,#8cb7de 0%,#c9a27a 45%,#e2b67c 70%,#d24a3a 100%)" role="img" aria-label="Travel collage of famous landmarks, luggage and a traveller relaxing in a beach chair"></div>
  <h3 class="band-heading" style="left:624px;top:82px">INTRODUCCION</h3>
  <p class="band-copy" style="left:624px;top:130px">Brixelvane es un nuevo tour operator receptivo de confianza especializado en el diseño y prestación de servicios personalizados de Incoming en destinos prístinos de la Ecorregión Sub-Antártica y Antártica Chilena.</p>
  <div class="btn" style="left:624px;top:258px;width:225px;height:43px">Contact Us for more Infomation</div>
</section>

<section class="band" style="top:1938px;height:389px;background:var(--band-b)">
  <h3 class="band-heading" style="left:157px;top:62px">QUIENES SOMOS</h3>
  <p class="band-copy" style="left:157px;top:112px">Somos una empresa conformada por un idóneo equipo de trabajo que consta de alta motivación, óptimo entrenamiento, elevado capital humano y cuyos integrantes poseen más de 10 años de experiencia trabajando en forma independiente en Turismo Receptivo Regional, Nacional e Internacional. En conjunto nos potenciamos y logramos satisfacer las altas demandas de servicios turísticos requeridos por nuestros clientes.</p>
  <div class="btn" style="left:157px;top:283px;width:140px;height:43px">Contact Us</div>
  <div class="cutout" style="left:800px;top:22px;width:400px;height:345px;border-radius:16px 0 0 16px;background:linear-gradient(135deg,#6d8bb0 0%,#4a6a92 40%,#b8a478 70%,#d6407a 100%)" role="img" aria-label="Denim jacket, sun hat, pink camera and passports laid out for a trip"></div>
</section>

<section class="band" style="top:2327px;height:391px;background:var(--band-c)">
  <h3 class="band-heading" style="left:157px;top:60px">MISION</h3>
  <p class="band-copy" style="left:157px;top:110px">Nuestra misión es ofrecer servicios de Turismo Receptivo para la Región de Magallanes y Antártica Chilena que cumplan con las exigencias de calidad y valor humano que nuestros clientes solicitan. Para lograrlo, trabajamos en conjunto con proveedores turísticos seleccionados y nos enfocamos hacia la excelencia de un servicio personalizado, otorgando con pasión, experiencia y responsabilidad a cada uno de nuestros clientes.</p>
  <div class="btn" style="left:157px;top:284px;width:218px;height:42px">Contact Us for more Infomation</div>
  <div class="cutout" style="left:664px;top:0;width:536px;height:391px;background:linear-gradient(135deg,#a9bf6a 0%,#82a046 40%,#5d6e3a 65%,#2e2e2e 100%)" role="img" aria-label="Green hiking backpack with pocket knife, binoculars, camera and paddle"></div>
</section>

<section class="band" style="top:2718px;height:389px;background:radial-gradient(ellipse at 70% 40%,#ffffff 0%,#f1f1f1 100%)">
  <div class="cutout" style="left:0;top:14px;width:300px;height:340px;border-radius:0 18px 18px 0;background:linear-gradient(160deg,#c07438 0%,#9a5526 55%,#6b3a18 100%)" role="img" aria-label="Vintage leather suitcase covered in travel stickers"></div>
  <h3 class="band-heading" style="left:624px;top:62px">VISION</h3>
  <p class="band-copy" style="left:624px;top:114px">Nuestra visión es crear una Plataforma de Servicios Logísticos y Turísticos para la Ecorregión Sub-Antártica y Antártica que una toda la oferta turística de la zona a través de una red local, nacional y global de proveedores, con el objetivo de mejorar, a través de la cuidadosa selección de prestadores, la accesibilidad por parte del cliente, la competitividad dentro del mercado, facilitando la inclusión de pequeñas y medianas empresas.</p>
  <div class="btn" style="left:624px;top:288px;width:134px;height:42px">Contact Us</div>
</section>

<section class="partners">
  <div class="partner" style="left:181px;top:3146px;width:64px;height:64px;border-radius:50%;border:2px solid #9a9a9a"></div>
  <div class="partner" style="left:583px;top:3142px;width:44px;height:66px;background:#8f8f8f"></div>
  <div class="partner" style="left:954px;top:3155px;width:72px;height:46px;border:2px solid #777"></div>
</section>

<footer class="site-footer">
  <div class="footer-brand"><span>BRIXELVANE</span></div>
  <div class="footer-col" style="left:389px">Home<br>Tours<br>Groups<br>Rent a Car<br>Flight<br>Contact</div>
  <div class="footer-col" style="left:602px">How to Book<br>Booking Terms<br>Privacy Policy</div>
  <div class="footer-contact">
    <div class="name">Frontdesk Brixelvane</div>
    <div>Finest tailor-made<br>travel experiences in patagonia</div>
    <div class="gap"></div>
    <div>Email: info@brixelvane.com<br>Phone: +56 61 2480915<br>Skype: Brixelvane<br>Web: www.brixelvane.com</div>
  </div>
  <div class="footer-rule"></div>
  <div class="copyright">© 2016 Brixelvane . All rights reserved.</div>
  <span class="social" style="left:962px"></span>
  <span class="social" style="left:980px"></span>
  <span class="social" style="left:998px"></span>
  <span class="social" style="left:1016px"></span>
  <span class="social" style="left:1034px"></span>
</footer>

</body>
</html>
```